Business card for hi tech component manufacturer, specialising in after market firearms components a
Tovin Industries (Ti)
Use same font as used in my logo
Owen Petrie
General Manager
Postal: PO Box 58491, Brackley, Christchurch 8245, New Zealand
Physical: 14 Garnet Street, Fenwick, Christchurch 8024, New Zealand
sales@tovin-works.example.nz
tovin-works.example.nz
Details are to be confirmed in future. Please allow space for Addresses, Phone, Cell, Email and Web address.
Hi Quill42,
You are the winner of the stationary project for Tovin Industries.
We have had some commercial issues with the company name Tovin, and as this is a start up company, we have changed the name.
The new Company name is ZENTH Industries. I have the new logo file, how do I send this to you?
As such I have a new set of address and company name for you to change for the final design.
And the only contact details we want on all the stationary options that you supplied are as follows:
Web: www.zenth.example.nz
Email address: sales@zenth.example.nz
Phone: +6429184306
Contact: Owen Petrie General Manager
Please advise, if you require a different file type, I have .ai, .eps, .gif, .pdf, .png, .psd, .jpg, .tif
I look forward to hearing from you.
Best regards,
Owen

```html
<!DOCTYPE html>
<html lang="en">
<head>
<meta charset="utf-8">
<title>Tovin Industries – Business Card</title>
<link href="https://fonts.googleapis.com/css2?family=Marcellus+SC&display=swap" rel="stylesheet">
<style>
  :root {
    --backdrop: #e4e6e8;
    --card: #fbfbfb;
    --brand: #34505f;
    --ink-soft: #5f7684;
    --rule: #8da0ab;
  }
  html, body {
    margin: 0;
    padding: 0;
    width: 1200px;
    height: 914px;
    overflow: hidden;
    background: var(--backdrop);
  }
  .stage {
    width: 1200px;
    height: 914px;
    display: flex;
    align-items: center;
    justify-content: center;
  }
  .business-card {
    position: relative;
    width: 1000px;
    height: 610px;
    background: var(--card);
    box-shadow: 0 6px 24px rgba(0,0,0,0.12);
    font-family: "Marcellus SC", serif;
    color: var(--brand);
    overflow: hidden;
  }
  .brand {
    position: absolute;
    left: 330px;
    top: 190px;
    display: flex;
    align-items: center;
    gap: 18px;
  }
  .brand-square {
    width: 26px;
    height: 26px;
    background: var(--brand);
  }
  .brand-name {
    font-size: 40px;
    letter-spacing: 3px;
    text-transform: uppercase;
    color: var(--brand);
  }
  .person {
    position: absolute;
    left: 330px;
    top: 318px;
    margin: 0;
    font-size: 24px;
    letter-spacing: 1.5px;
    color: var(--ink-soft);
  }
  .person .divider {
    display: inline-block;
    width: 1px;
    height: 22px;
    background: var(--rule);
    margin: 0 14px;
    vertical-align: -3px;
  }
  .contact {
    position: absolute;
    left: 34px;
    right: 34px;
    bottom: 74px;
    font-size: 11px;
    letter-spacing: 0.2px;
    color: var(--brand);
    line-height: 22px;
  }
  .contact-line {
    display: flex;
    align-items: center;
    white-space: nowrap;
  }
  .contact-item {
    display: inline-flex;
    align-items: center;
    gap: 4px;
    margin-right: 9px;
  }
  .contact-item:last-child {
    margin-right: 0;
  }
  .icon {
    width: 12px;
    height: 12px;
    flex: none;
  }
</style>
</head>
<body>
<main class="stage">
  <article class="business-card">
    <div class="brand">
      <span class="brand-square"></span>
      <span class="brand-name">Tovin Industries</span>
    </div>

    <p class="person">Owen Petrie<span class="divider"></span>General Manager</p>

    <div class="contact">
      <div class="contact-line">
        <span class="contact-item">
          <svg class="icon" viewBox="0 0 12 12"><circle cx="6" cy="6" r="6" fill="var(--brand)"/><path d="M6 2.5a2.2 2.2 0 0 0-2.2 2.2C3.8 6.4 6 9.5 6 9.5s2.2-3.1 2.2-4.8A2.2 2.2 0 0 0 6 2.5z" fill="#fff"/></svg>
          PO Box 58491, Brackley, Christchurch 8245, New Zealand
        </span>
      </div>
      <div class="contact-line">
        <span class="contact-item">
          <svg class="icon" viewBox="0 0 12 12"><circle cx="6" cy="6" r="6" fill="var(--brand)"/><path d="M4 3l1.2 1.6-.6.8c.4.8 1 1.4 1.8 1.8l.8-.6L8.8 7.8 8 9C5.6 8.6 3.4 6.4 3 4z" fill="#fff"/></svg>
          +64 3 555 0142
        </span>
        <span class="contact-item">
          <svg class="icon" viewBox="0 0 12 12"><circle cx="6" cy="6" r="6" fill="var(--brand)"/><rect x="4.2" y="2.5" width="3.6" height="7" rx="0.6" fill="#fff"/></svg>
          +64 29 184 306
        </span>
        <span class="contact-item">
          <svg class="icon" viewBox="0 0 12 12"><circle cx="6" cy="6" r="6" fill="var(--brand)"/><path d="M6 2.5a2.2 2.2 0 0 0-2.2 2.2C3.8 6.4 6 9.5 6 9.5s2.2-3.1 2.2-4.8A2.2 2.2 0 0 0 6 2.5z" fill="#fff"/></svg>
          14 Garnet Street, Fenwick, Christchurch 8024, New Zealand
        </span>
        <span class="contact-item">
          <svg class="icon" viewBox="0 0 12 12"><circle cx="6" cy="6" r="6" fill="var(--brand)"/><rect x="3" y="4" width="6" height="4.2" fill="#fff"/><path d="M3 4l3 2.3L9 4" fill="none" stroke="var(--brand)" stroke-width="0.7"/></svg>
          sales@tovin-works.example.nz
        </span>
        <span class="contact-item">
          <svg class="icon" viewBox="0 0 12 12"><circle cx="6" cy="6" r="6" fill="var(--brand)"/><circle cx="6" cy="6" r="3" fill="none" stroke="#fff" stroke-width="0.8"/><path d="M3 6h6M6 3c-1.3 1.6-1.3 4.4 0 6M6 3c1.3 1.6 1.3 4.4 0 6" fill="none" stroke="#fff" stroke-width="0.6"/></svg>
          www.tovin-works.example.nz
        </span>
      </div>
    </div>
  </article>
</main>
</body>
</html>
```